Website Design for Harlow Crest Advisors – Professional, Modern, and Sustainable Energy Consulting

Harlow Crest Advisors is a leading consultancy specializing in sustainable energy solutions. We are seeking a professional and visually appealing Squarespace website design to showcase our expertise and services. The website should reflect our brand identity, as defined by our new logo, and provide an engaging user experience. Please read carefully the attached document "Website product requirement rev 1.pdf".

```html
<!DOCTYPE html>
<html lang="en">
<head>
<meta charset="utf-8">
<title>Harlow Crest Advisors – Solar PV Project Development Advisory</title>
<link rel="stylesheet" href="https://fonts.googleapis.com/css2?family=Poppins:wght@400;500;600&display=swap">
<style>
:root{
  --green:#2ea84f;
  --navy:#1b2636;
  --ink:#111111;
  --text:#222222;
  --white:#ffffff;
  --sky-top:#6f86b3;
  --sky-mid:#a9b7cf;
  --field:#4d6a34;
  --field-dark:#2f4620;
}
*{margin:0;padding:0;box-sizing:border-box}
html,body{width:1200px;height:4354px;overflow:hidden;background:var(--white)}
body{font-family:"Poppins",sans-serif;color:var(--text);position:relative}
.abs{position:absolute}
.btn{position:absolute;display:flex;align-items:center;justify-content:center;background:var(--green);color:var(--white);font-size:11.5px;font-weight:500;letter-spacing:1.6px;text-transform:uppercase;text-decoration:none}
/* hero */
.hero{position:absolute;left:0;top:0;width:1200px;height:643px;background:linear-gradient(180deg,var(--sky-top) 0%,var(--sky-mid) 42%,#8c9a7d 55%,var(--field) 70%,var(--field-dark) 100%)}
.brand{position:absolute;left:137px;top:26px;display:flex;align-items:center;gap:10px;color:var(--white);font-size:25px;font-weight:600}
.brand-dot{width:44px;height:44px;border-radius:50%;background:var(--green)}
.nav{position:absolute;top:54px;left:428px;display:flex;gap:26px;font-size:11.5px;font-weight:500;color:var(--white)}
.nav .active{color:var(--green)}
.hero-title{position:absolute;left:132px;top:386px;width:620px;font-size:36px;line-height:43px;font-weight:600;color:var(--white)}
.hero-sub{position:absolute;left:132px;top:478px;font-size:23px;color:var(--white)}
/* sections */
h2{font-weight:500;color:var(--ink)}
.center{left:0;width:1200px;text-align:center}
.who-lead{top:826px;font-size:20px;line-height:29px}
.who-body{top:904px;left:200px;width:800px;text-align:center;font-size:12.5px;line-height:29px}
.exp-photo{left:139px;top:1179px;width:449px;height:506px;background:linear-gradient(160deg,#c9ccc4 0%,#a8ad9f 45%,#d5682f 80%,#9a4a24 100%)}
.map{left:612px;top:1775px;width:449px;height:508px;background:linear-gradient(135deg,#f1f1f1,#e3e3e3)}
.body-copy{font-size:16px;line-height:29px;color:var(--text)}
.band{position:absolute;left:0;width:1200px;background:var(--navy);color:var(--white)}
.band h2{color:var(--white)}
.service{position:absolute;top:2590px;width:220px;text-align:center;color:var(--white)}
.service svg{display:block;margin:0 auto 36px}
.service p{font-size:18px;line-height:22px;font-weight:500}
.project-photo{position:absolute;top:3204px;width:211px;height:304px}
.project-label{position:absolute;top:3520px;font-size:28px;font-weight:500;color:var(--ink)}
.footer h4{position:absolute;top:4188px;font-size:18px;font-weight:500;color:var(--ink)}
.flink{position:absolute;font-size:12.5px;color:var(--green);text-decoration:underline}
.social{position:absolute;top:4270px;width:16px;height:16px;border-radius:50%;border:2px solid var(--ink)}
</style>
</head>
<body>

<header class="hero">
  <div role="img" aria-label="Solar panel rows across a grassy field under a blue sky" class="abs" style="inset:0"></div>
  <div class="brand"><span class="brand-dot"></span>Harlow Crest Advisors</div>
  <nav class="nav"><span class="active">Home</span><span>About</span><span>Services</span><span>Projects</span><span>Contact Us</span></nav>
  <a class="btn" style="left:899px;top:50px;width:163px;height:40px;font-size:14px">Get Started</a>
  <h1 class="hero-title">Solar pv project development advisory services</h1>
  <p class="hero-sub">Achieving success one hour at a time</p>
</header>

<section class="who">
  <h2 class="abs center" style="top:740px;font-size:44px">Who We Are</h2>
  <p class="abs center who-lead">Starting as novices in 1993, we have worked on every aspect of a project's life cycle,<br>from concept to commissioning, in order to become today's experts.</p>
  <p class="abs who-body">Daniel Reyes is a dynamic, solution-focused technical leader with more than 24 years of international experience in solar PV, project management, installation and engineering across LATAM, Spain, Canada and USA. Daniel has a proven track record delivering and directing key technical aspects in support of business development and project development. Daniel excels at guiding development engineering and system optimization.</p>
  <a class="btn" style="left:505px;top:1056px;width:189px;height:48px">Learn More</a>
</section>

<section class="experience">
  <div class="abs exp-photo" role="img" aria-label="Field engineer in a hard hat and safety vest at a wind farm"></div>
  <h2 class="abs" style="left:645px;top:1328px;font-size:44px">Our Experience</h2>
  <p class="abs body-copy" style="left:647px;top:1410px;width:380px">We are ready to help you to succeed, from Project Development  or M&amp;A to each step of the way through the project's entire life cycle.</p>
</section>

<section class="options">
  <h2 class="abs" style="left:139px;top:1884px;font-size:46px;line-height:56px">In-person and<br>remote options</h2>
  <p class="abs body-copy" style="left:139px;top:2030px;width:390px">Contact us to learn more about how we will be able to help you with project development, M&amp;A or project execution. BACK</p>
  <div class="abs map" role="img" aria-label="Map of the central United States around Colorado, Nebraska and Kansas"></div>
</section>

<section class="band" style="top:2368px;height:647px">
  <h2 class="abs center" style="top:60px;font-size:46px">Our Services</h2>
</section>
<div class="service" style="left:133px">
  <svg width="110" height="110" viewBox="0 0 110 110" fill="none" stroke="#fff" stroke-width="3"><circle cx="30" cy="45" r="8"/><circle cx="55" cy="38" r="8"/><circle cx="80" cy="45" r="8"/><rect x="45" y="8" width="28" height="16" rx="3"/><rect x="18" y="62" width="74" height="10"/><path d="M22 72v30M88 72v30M15 60v40M95 60v40"/></svg>
  <p>Project Development Technical Advisor</p>
</div>
<div class="service" style="left:374px">
  <svg width="110" height="110" viewBox="0 0 110 110" fill="none" stroke="#fff" stroke-width="3"><path d="M10 60l40-25 15 10 35-25"/><path d="M88 18h12v12"/><rect x="20" y="68" width="12" height="22"/><rect x="45" y="55" width="12" height="35"/><rect x="70" y="45" width="12" height="45"/><path d="M10 92h92"/><circle cx="58" cy="98" r="9"/></svg>
  <p>Performing System Optimization</p>
</div>
<div class="service" style="left:595px">
  <svg width="110" height="110" viewBox="0 0 110 110" fill="none" stroke="#fff" stroke-width="3"><circle cx="55" cy="55" r="36"/><path d="M30 80c0-25 15-35 35-35-2 22-15 35-35 35z"/><path d="M62 22l-8 16h10l-8 16"/><path d="M12 30l10 6M98 80l-10-6"/></svg>
  <p>Running Energy Simulation</p>
</div>
<div class="service" style="left:838px">
  <svg width="110" height="110" viewBox="0 0 110 110" fill="none" stroke="#fff" stroke-width="3"><circle cx="55" cy="20" r="7"/><path d="M55 4v5M55 31v5M39 20h5M66 20h5"/><path d="M22 45h66l10 30H12z"/><path d="M44 45l-4 30M66 45l4 30M16 60h78"/><path d="M55 75v25M40 100h30"/></svg>
  <p>Designing the Plant Layout</p>
</div>
<a class="btn" style="left:505px;top:2850px;width:189px;height:48px">Learn More</a>

<section class="projects">
  <h2 class="abs center" style="top:3092px;font-size:46px">Our Projects</h2>
  <div class="project-photo" style="left:139px;background:linear-gradient(180deg,#7fa3d4,#b9c5c9 45%,#8a7a4a 75%,#5b5a3e)" role="img" aria-label="Drilling rig on a hillside site"></div>
  <div class="project-photo" style="left:376px;background:linear-gradient(180deg,#f2f2f2 20%,#8f9a9c 35%,#b4b0a6 60%,#6e6e6a)" role="img" aria-label="Solar array construction site with service truck"></div>
  <div class="project-photo" style="left:613px;background:linear-gradient(180deg,#c9d3de,#8a9199 40%,#3e4c63 60%,#5f7a3e)" role="img" aria-label="Rooftop solar panels on an industrial building"></div>
  <div class="project-photo" style="left:850px;background:linear-gradient(135deg,#8d6a54,#4c5468 45%,#a47b5f 70%,#3e4660)" role="img" aria-label="Ground-mounted solar panel rows on red soil"></div>
  <p class="project-label" style="left:141px">Drilling</p>
  <p class="project-label" style="left:380px">Chico,CA</p>
  <p class="project-label" style="left:615px">Chico,CA</p>
  <p class="project-label" style="left:848px">Prescot,CA</p>
  <a class="btn" style="left:505px;top:3608px;width:189px;height:48px">Learn More</a>
</section>

<section class="band" style="top:3735px;height:397px">
  <h2 class="abs center" style="top:78px;font-size:52px;line-height:63px">Get started with<br>Harlow Crest, today</h2>
  <a class="btn" style="left:477px;top:253px;width:247px;height:48px">Book a Consultation</a>
</section>

<footer class="footer">
  <h4 style="left:165px">Stay in touch</h4>
  <h4 style="left:446px">Questions?</h4>
  <a class="flink" style="left:449px;top:4224px">Contact Us</a>
  <a class="flink" style="left:682px;top:4192px">Home</a>
  <a class="flink" style="left:682px;top:4224px">About</a>
  <a class="flink" style="left:682px;top:4254px">Services</a>
  <a class="flink" style="left:843px;top:4192px">Our Experience</a>
  <a class="flink" style="left:843px;top:4224px">Projects</a>
  <a class="flink" style="left:843px;top:4254px">Get Started</a>
  <p class="abs" style="left:167px;top:4268px;font-size:12px;color:var(--ink)">© 2024  |  www.harlowcrest.com</p>
  <span class="social" style="left:447px"></span>
  <span class="social" style="left:485px"></span>
</footer>

</body>
</html>
```